Kestrelwood Pathways Agency business cards

Australian company about to start offering its services. We recruit international students to come to study English, vocational education and postgraduate courses in Australia. We help them find the institution and select the right city they want to come to Australia. We are a young, online oriented and supportive agency. Our clients are between 18 and 35 years old, mainly University students, young professionals or people with work experience. We provide much more information that any other agency offer. We administrate a Facebook group with more than 11.000 members that daily ask questions about general information when coming to Australia, while they are here and even after they leave the country

Target Market(s)

International students from South America, Central America and Europe

Industry/Entity Type

Student

Contact Information for Business Card

Tomas Brevik
Managing Director
tomas@velmorin.com.au
www.velmorin.com.au
+61 491058263
Melbourne, Australia

Font styles to use
Serif
Sans Serif

Colors

Designer to choose colors to be used in the design.

Requirements
Must have
• Horizontal design
• Standard business card size and shape. If font uses green or yellow colours, they will have to match the ones from the logo
Nice to have
• UPDATE: Use the contents of the green image to design one of the card sides. Use our logo in the background of that side as watermark.
• Passport image, or immigration stamps. A picture of the Yarra River (from Melbourne) would be cool as well.
Should not have
• Non-standard business card size and shape
• Not black as the background colour of any sides as we are not a VIP agency or a hight class service. We are orientes to young people and they like colours, pictures, something attractive.
• Vertical design
• NO YELLOW or BLACK AS THE BACKGROUND COLOUR OF ANY SIDE OF THE BIZ CARD

```html
<!DOCTYPE html>
<html lang="en">
<head>
<meta charset="utf-8">
<title>Kestrelwood Pathways Agency – Business Cards</title>
<link href="https://fonts.googleapis.com/css2?family=Open+Sans:wght@400;700&display=swap" rel="stylesheet">
<style>
  :root {
    --page-bg: #ecebe7;
    --card-front-start: #1e7a4e;
    --card-front-end: #2f8f63;
    --card-light: #ffffff;
    --brand-green: #1e7a4e;
    --brand-green-soft: #4f9a7e;
    --brand-yellow: #e8c531;
    --text-dark: #2a2a2a;
    --text-grey: #444444;
    --text-light: #ffffff;
  }
  * { margin: 0; padding: 0; box-sizing: border-box; }
  html, body {
    width: 1200px; height: 800px; overflow: hidden;
    background: var(--page-bg);
    font-family: "Open Sans", Arial, sans-serif;
  }
  .sheet {
    width: 1200px; height: 800px;
    display: flex; align-items: center; justify-content: center; gap: 60px;
  }
  .card {
    position: relative;
    width: 530px; height: 303px;
    border-radius: 22px;
    overflow: hidden;
    box-shadow: 0 6px 18px rgba(0,0,0,0.18);
  }
  /* Front */
  .card-front {
    background: linear-gradient(135deg, var(--card-front-start), var(--card-front-end));
  }
  .front-watermark {
    position: absolute; left: 50%; top: 50%;
    transform: translate(-50%, -50%);
    font-size: 96px; font-weight: 700;
    color: rgba(255,255,255,0.07);
    white-space: nowrap;
  }
  .front-wordmark {
    position: absolute; left: 50%; top: 50%;
    transform: translate(-50%, -50%);
    display: flex; align-items: center; gap: 14px;
  }
  .wordmark-dot {
    width: 22px; height: 22px; border-radius: 50%;
    background: var(--brand-yellow);
  }
  .wordmark-name {
    font-size: 56px; font-weight: 700;
    color: var(--text-light);
    letter-spacing: 0.5px;
    line-height: 1;
  }
  /* Back */
  .card-back { background: var(--card-light); }
  .back-wordmark {
    position: absolute; right: 40px; top: 52px;
    display: flex; align-items: center; gap: 10px;
  }
  .back-wordmark .wordmark-name { font-size: 40px; color: var(--brand-green); }
  .back-wordmark .wordmark-dot { width: 16px; height: 16px; }
  .person {
    position: absolute; left: 0; top: 126px;
    padding-left: 26px;
  }
  .person::before {
    content: ""; position: absolute; left: 0; top: 4px;
    width: 12px; height: 44px; background: var(--brand-green);
  }
  .person-name { font-size: 22px; color: var(--text-dark); line-height: 1.15; }
  .person-name strong { font-weight: 700; }
  .person-role { font-size: 14px; color: var(--brand-yellow); }
  .contacts {
    position: absolute; left: 26px; top: 186px;
    list-style: none;
    font-size: 14px; color: var(--text-grey);
  }
  .contacts li { display: flex; align-items: center; gap: 10px; height: 22px; }
  .contact-icon {
    width: 16px; height: 16px; border-radius: 3px;
    background: var(--brand-green);
    display: flex; align-items: center; justify-content: center;
  }
  .contact-icon svg { width: 10px; height: 10px; }
  .web-band {
    position: absolute; left: 0; right: 0; bottom: 0; height: 42px;
    background: linear-gradient(90deg, var(--brand-green), var(--brand-green-soft));
    display: flex; align-items: center; padding-left: 26px;
  }
  .web-band span { color: var(--text-light); font-size: 14px; opacity: 0.9; }
</style>
</head>
<body>
<main class="sheet">
  <section class="card card-front" aria-label="Card front">
    <div class="front-watermark" aria-hidden="true">Velmorin</div>
    <div class="front-wordmark">
      <span class="wordmark-dot"></span>
      <span class="wordmark-name">Velmorin</span>
    </div>
  </section>

  <section class="card card-back" aria-label="Card back">
    <div class="back-wordmark">
      <span class="wordmark-dot"></span>
      <span class="wordmark-name">Velmorin</span>
    </div>
    <div class="person">
      <p class="person-name">Tomas <strong>Brevik</strong></p>
      <p class="person-role">Managing Director</p>
    </div>
    <ul class="contacts">
      <li>
        <span class="contact-icon"><svg viewBox="0 0 10 10"><path d="M2 1h2l1 2-1 1a5 5 0 0 0 2 2l1-1 2 1v2a1 1 0 0 1-1 1A8 8 0 0 1 1 2a1 1 0 0 1 1-1z" fill="#fff"/></svg></span>
        +61 491058263
      </li>
      <li>
        <span class="contact-icon"><svg viewBox="0 0 10 10"><rect x="1" y="2.5" width="8" height="5.5" fill="none" stroke="#fff" stroke-width="1"/><path d="M1 2.5l4 3 4-3" fill="none" stroke="#fff" stroke-width="1"/></svg></span>
        tomas@velmorin.com.au
      </li>
      <li>
        <span class="contact-icon"><svg viewBox="0 0 10 10"><path d="M5 9.5S2 6 2 4a3 3 0 0 1 6 0c0 2-3 5.5-3 5.5z" fill="#fff"/><circle cx="5" cy="4" r="1" fill="#1e7a4e"/></svg></span>
        Melbourne, Australia
      </li>
    </ul>
    <div class="web-band"><span>www.velmorin.com.au</span></div>
  </section>
</main>
</body>
</html>
```